Invitation Card for Wedding

An invitation card for a wedding is needed.

This competition is to decide the designer who is going to do the real card design. Project budget is in between 30-50 euro. Project time is 1 week after the end of the competition.

You can submit your best available designs for invitation cards. Or desing a card for the weeding of "Selin" and "Burak" with imaginary informations such as place / date / time.

Edit: please check if you can use the figures at the attached images. No need to do a final design for the moment, but I would like to see that you are capable of using and creating nice cards with them.

The competition prize will be distributed fairly.
Good luck

```html
<!DOCTYPE html>
<html lang="en">
<head>
<meta charset="utf-8">
<title>Selin &amp; Burak – Wedding Invitation</title>
<link rel="stylesheet" href="https://fonts.googleapis.com/css2?family=Great+Vibes&display=swap">
<style>
  :root {
    --frame-top: #e2a21c;
    --frame-light: #f8f08a;
    --frame-mid: #d8841a;
    --frame-dark: #8e3206;
    --frame-bottom: #e6a018;
    --paper: #fdf9d8;
    --ink: #8a2a10;
    --gold-soft: #f0d79a;
    --gold-mid: #e3b552;
    --gold-deep: #c98a22;
  }
  html, body {
    margin: 0;
    padding: 0;
    width: 876px;
    height: 1200px;
    overflow: hidden;
    background: #ffffff;
  }
  .card {
    position: relative;
    width: 876px;
    height: 1200px;
    background: #ffffff;
  }
  .card__frame {
    position: absolute;
    left: 33px;
    top: 33px;
    width: 810px;
    height: 1127px;
    background: linear-gradient(180deg,
      var(--frame-top) 0%,
      var(--frame-light) 24%,
      var(--frame-mid) 40%,
      var(--frame-dark) 60%,
      var(--frame-mid) 82%,
      var(--frame-bottom) 100%);
  }
  .card__paper {
    position: absolute;
    left: 63px;
    top: 60px;
    width: 752px;
    height: 1073px;
    background: var(--paper);
    box-shadow: 0 0 0 2px #fffbe6;
  }
  .ornament {
    position: absolute;
  }
  .ornament--floral-top {
    left: 66px;
    top: 62px;
    width: 400px;
    height: 420px;
    background: radial-gradient(ellipse 60% 55% at 32% 38%, rgba(240,215,154,0.9) 0%, rgba(240,215,154,0.45) 50%, rgba(253,249,216,0) 100%);
  }
  .ornament--floral-bottom {
    left: 432px;
    top: 760px;
    width: 383px;
    height: 372px;
    background: radial-gradient(ellipse 60% 55% at 66% 64%, rgba(240,215,154,0.9) 0%, rgba(240,215,154,0.45) 50%, rgba(253,249,216,0) 100%);
  }
  .band {
    position: absolute;
    width: 110px;
    border-left: 2px solid var(--gold-deep);
    border-right: 2px solid var(--gold-deep);
    box-sizing: border-box;
  }
  .band__fill {
    position: absolute;
    left: 10px;
    right: 10px;
    top: 6px;
    bottom: 6px;
    background: linear-gradient(90deg, var(--gold-mid), var(--gold-soft) 50%, var(--gold-mid));
    opacity: 0.85;
  }
  .band--right {
    left: 720px;
    top: 64px;
    height: 602px;
    border-bottom: 2px solid var(--gold-deep);
  }
  .band--left {
    left: 70px;
    top: 570px;
    height: 600px;
    border-top: 2px solid var(--gold-deep);
  }
  .card__text {
    position: absolute;
    left: 0;
    width: 876px;
    margin: 0;
    text-align: center;
    font-family: "Great Vibes", cursive;
    font-weight: 400;
    color: var(--ink);
    line-height: 1;
    white-space: nowrap;
  }
  .card__name--first  { top: 247px; font-size: 136px; left: 30px; }
  .card__name--second { top: 402px; font-size: 136px; left: 20px; }
  .card__title--one   { top: 608px; font-size: 108px; left: 0; }
  .card__title--two   { top: 748px; font-size: 108px; left: 0; }
  .card__title--three { top: 873px; font-size: 108px; left: 0; }
</style>
</head>
<body>
  <main class="card">
    <div class="card__frame"></div>
    <div class="card__paper"></div>

    <div class="ornament ornament--floral-top" role="img" aria-label="Golden line-drawn flowers and leaves in the top-left corner"></div>
    <div class="ornament band band--right" role="img" aria-label="Vertical golden floral scroll band on the right"><div class="band__fill"></div></div>
    <div class="ornament band band--left" role="img" aria-label="Vertical golden floral scroll band on the left"><div class="band__fill"></div></div>
    <div class="ornament ornament--floral-bottom" role="img" aria-label="Golden line-drawn flowers and leaves in the bottom-right corner"></div>

    <h1 class="card__text card__name--first">Selin</h1>
    <p class="card__text card__name--second">&amp; Burak</p>
    <p class="card__text card__title--one">Invitation</p>
    <p class="card__text card__title--two">Card for</p>
    <p class="card__text card__title--three">Wedding</p>
  </main>
</body>
</html>
```